Income Tax Flyer - Updates Needed

Just need to update this flyer design and give it a new look. We would like to keep all the same wording but make it stand out a little more. Our selling point is the "Same Day Tax Advance up to $6,000"

Industry/Entity Type

Lending, Small Loans, Tax Services, Title Loans, Personal Loans

```html
<!DOCTYPE html>
<html lang="en">
<head>
<meta charset="utf-8">
<title>Same Day Tax Advance Flyer</title>
<link href="https://fonts.googleapis.com/css2?family=Montserrat:wght@400;500;600;700;800;900&display=swap" rel="stylesheet">
<style>
  :root{
    --bg:#ececec;
    --paper:#ffffff;
    --green:#0d4a27;
    --green-icon:#13652f;
    --red:#e0232f;
    --red-dark:#c81e29;
    --ink:#111111;
    --bar:#141414;
    --rule:#3a3a3a;
  }
  *{margin:0;padding:0;box-sizing:border-box}
  html,body{width:1200px;height:2311px;overflow:hidden}
  body{background:var(--bg);font-family:'Montserrat',sans-serif;position:relative}
  .flyer{
    position:absolute;left:100px;top:463px;width:1000px;height:1385px;
    background:var(--paper);box-shadow:-18px 18px 40px rgba(0,0,0,.18);
  }
  .brand{position:absolute;top:70px;left:0;width:100%;display:flex;justify-content:center;align-items:center;gap:16px}
  .brand-dot{width:22px;height:22px;border-radius:50%;background:var(--green)}
  .brand-name{font-weight:700;color:var(--green);font-size:44px;letter-spacing:1px;line-height:1.1;text-align:center}
  .brand-name small{display:block;font-size:16px;letter-spacing:6px;font-weight:700}
  .headline{position:absolute;top:222px;width:100%;text-align:center;font-weight:800;font-size:50px;color:var(--ink);letter-spacing:.5px;z-index:2}
  .amount{position:absolute;top:296px;width:100%;text-align:center;font-weight:900;font-size:106px;color:var(--green);letter-spacing:1px;line-height:1.15;white-space:nowrap;z-index:2}
  .photo{
    position:absolute;top:410px;left:0;width:100%;height:422px;z-index:1;
    background:linear-gradient(180deg,#ffffff 0%,#eef1f4 25%,#d9dfe5 60%,#c9cfd6 85%,#e4e8ec 100%);
  }
  .banner{
    position:absolute;top:832px;left:0;width:100%;height:153px;
    background:linear-gradient(90deg,var(--red) 0%,var(--red-dark) 100%);
    color:#fff;text-align:center;padding-top:34px;
  }
  .banner-lead{font-weight:500;font-size:40px;letter-spacing:2px;line-height:1.2}
  .banner-strong{font-weight:800;font-size:40px;letter-spacing:1.5px;line-height:1.2}
  .features{position:absolute;top:1060px;left:0;width:100%;height:94px}
  .feature{position:absolute;top:0;display:flex;align-items:center;gap:30px}
  .feature-icon{width:94px;height:94px;border-radius:50%;background:var(--green-icon);display:flex;align-items:center;justify-content:center;flex:none}
  .feature-text{font-size:24px;font-weight:500;color:#222;line-height:1.05;white-space:nowrap}
  .contact-head{position:absolute;top:1212px;left:62px;right:62px;display:flex;align-items:center;gap:18px}
  .contact-head .rule{flex:1;height:2px;background:var(--rule)}
  .contact-head h2{color:var(--red);font-weight:800;font-size:32px;letter-spacing:1.5px;white-space:nowrap}
  .contact-bar{position:absolute;top:1275px;left:0;width:100%;height:69px;background:var(--bar);display:flex;align-items:center;padding-left:78px;color:#fff;white-space:nowrap}
  .phone{display:flex;align-items:center;gap:16px;font-weight:700;font-size:32px;letter-spacing:.5px;margin-right:32px;white-space:nowrap;flex:none}
  .address{display:flex;align-items:center;gap:8px;font-size:17px;font-weight:500;margin-right:32px;letter-spacing:.3px;white-space:nowrap;flex:none}
</style>
</head>
<body>
  <article class="flyer">
    <header class="brand">
      <span class="brand-dot"></span>
      <div class="brand-name">Keystone<small>FINANCIAL GROUP</small></div>
    </header>

    <h1 class="headline">SAME DAY TAX ADVANCE</h1>
    <p class="amount">UP TO $6,000</p>

    <div class="photo" role="img" aria-label="Photo of two smiling colleagues working together on laptops in a bright office"></div>

    <section class="banner">
      <p class="banner-lead">FILE YOUR TAXES AND APPLY FOR</p>
      <p class="banner-strong">AN EASY ADVANCE</p>
    </section>

    <section class="features">
      <div class="feature" style="left:78px">
        <div class="feature-icon">
          <svg width="60" height="60" viewBox="0 0 60 60" fill="none" stroke="#fff" stroke-width="2.6" stroke-linecap="round" stroke-linejoin="round">
            <path d="M14 14c-3 3-3 9 2 17s14 16 20 16c4 0 6-2 7-4l-6-6-5 3c-4-2-9-7-11-11l3-5-6-6c-2 0-3 1-4 2z"/>
            <text x="31" y="26" fill="#fff" stroke="none" font-family="Montserrat,sans-serif" font-weight="700" font-size="16">24</text>
            <path d="M30 8a20 20 0 0 1 20 20"/>
          </svg>
        </div>
        <p class="feature-text">Available<br>in 24 hours<br>or less</p>
      </div>
      <div class="feature" style="left:396px">
        <div class="feature-icon">
          <svg width="60" height="60" viewBox="0 0 60 60" fill="none" stroke="#fff" stroke-width="2.4" stroke-linecap="round" stroke-linejoin="round">
            <rect x="13" y="10" width="26" height="36" rx="2"/>
            <circle cx="26" cy="21" r="6"/>
            <path d="M26 18v6M18 32h16M18 38h10"/>
            <rect x="32" y="34" width="18" height="12" rx="2"/>
            <circle cx="41" cy="40" r="2.5"/>
          </svg>
        </div>
        <p class="feature-text">Choose your<br>Loan amount</p>
      </div>
      <div class="feature" style="left:716px">
        <div class="feature-icon">
          <svg width="60" height="60" viewBox="0 0 60 60" fill="none" stroke="#fff" stroke-width="2.6" stroke-linecap="round" stroke-linejoin="round">
            <circle cx="30" cy="33" r="16"/>
            <path d="M26 11h8M30 11v6M44 18l3-3"/>
            <path d="M23 33l5 5 9-10"/>
          </svg>
        </div>
        <p class="feature-text">Quick<br>and Easy</p>
      </div>
    </section>

    <div class="contact-head">
      <span class="rule"></span>
      <h2>CONTACT US</h2>
      <span class="rule"></span>
    </div>

    <footer class="contact-bar">
      <span class="phone">
        <svg width="26" height="26" viewBox="0 0 24 24" fill="none" stroke="#fff" stroke-width="1.8" stroke-linecap="round" stroke-linejoin="round"><path d="M5 4h4l2 5-2.5 1.5a11 11 0 0 0 5 5L15 13l5 2v4a2 2 0 0 1-2 2A16 16 0 0 1 3 6a2 2 0 0 1 2-2z"/></svg>
        555 010 2040
      </span>
      <span class="address"><svg width="14" height="18" viewBox="0 0 14 18" fill="none" stroke="#fff" stroke-width="1.6"><path d="M7 17s6-6 6-10A6 6 0 0 0 1 7c0 4 6 10 6 10z"/><circle cx="7" cy="7" r="2"/></svg>ADREES LINE 1</span>
      <span class="address"><svg width="14" height="18" viewBox="0 0 14 18" fill="none" stroke="#fff" stroke-width="1.6"><path d="M7 17s6-6 6-10A6 6 0 0 0 1 7c0 4 6 10 6 10z"/><circle cx="7" cy="7" r="2"/></svg>ADREES LINE 2</span>
      <span class="address"><svg width="14" height="18" viewBox="0 0 14 18" fill="none" stroke="#fff" stroke-width="1.6"><path d="M7 17s6-6 6-10A6 6 0 0 0 1 7c0 4 6 10 6 10z"/><circle cx="7" cy="7" r="2"/></svg>ADREES LINE 3</span>
    </footer>
  </article>
</body>
</html>
```